Velqor5 Business Card - Health

Velqor5 maximizes value from the health data of its clients, including doctors, HMOs, and patients. I have attached the Velqor5 logo as an ai and eps file.
Target Market(s)
Health, HMO, Healthcare, Data, Big Data, Data Analytics
Industry/Entity Type
Business
Requirements
Must have
- At least one side should have some white on it so that we can write on it.

```html
<!DOCTYPE html>
<html lang="en">
<head>
<meta charset="utf-8">
<title>Velqor5 Business Card</title>
<link rel="stylesheet" href="https://fonts.googleapis.com/css2?family=Arimo:ital,wght@0,400;0,700;1,400&display=swap">
<style>
  :root {
    --bg: #2a2b2d;
    --card-white: #ffffff;
    --card-dark: #1f2022;
    --blue: #0a6fd4;
    --blue-light: #2a8ff0;
    --ink: #3a3a3a;
    --ink-soft: #555;
    --grey-url: #8a8a8a;
  }
  * { box-sizing: border-box; margin: 0; padding: 0; }
  html, body { width: 1200px; height: 871px; overflow: hidden; }
  body {
    background: var(--bg);
    font-family: "Arimo", Arial, sans-serif;
    position: relative;
  }
  .card {
    position: absolute;
    width: 540px;
    height: 309px;
    top: 281px;
    border-radius: 3px;
    box-shadow: 0 10px 30px rgba(0,0,0,0.45);
    overflow: hidden;
  }
  .card-back { left: 40px; background: var(--card-dark); }
  .card-front { left: 620px; background: var(--card-white); }

  /* back */
  .back-brand {
    position: absolute;
    left: 0; right: 0; top: 110px;
    display: flex; align-items: center; justify-content: center; gap: 14px;
  }
  .back-brand .dot {
    width: 38px; height: 38px; border-radius: 50%; background: var(--blue);
  }
  .back-brand .name {
    font-size: 52px; color: var(--blue-light); font-weight: 400;
  }
  .back-url {
    position: absolute; left: 0; right: 0; top: 250px;
    text-align: center; color: var(--grey-url);
    font-size: 12px; letter-spacing: 5px;
  }

  /* front */
  .name-band {
    position: absolute; left: 0; top: 26px;
    width: 320px; height: 48px;
    background: linear-gradient(90deg, var(--blue), var(--blue-light));
    color: #fff; padding: 6px 0 0 28px;
  }
  .name-band .person { font-size: 18px; font-weight: 700; display: block; }
  .name-band .role { font-size: 13px; font-style: italic; display: block; margin-top: 1px; }
  .front-brand {
    position: absolute; left: 332px; top: 27px;
    display: flex; align-items: center; gap: 12px;
  }
  .front-brand .dot {
    width: 40px; height: 40px; border-radius: 50%;
    background: var(--blue-light); border: 3px solid var(--blue);
  }
  .front-brand .name { font-size: 40px; color: var(--ink); font-weight: 400; }

  .contacts {
    position: absolute; left: 34px; top: 180px;
    list-style: none; font-size: 13px; color: var(--ink-soft);
  }
  .contacts li { display: flex; align-items: center; gap: 8px; height: 19px; }
  .contacts svg { width: 14px; height: 14px; fill: var(--blue); }

  .address {
    position: absolute; right: 30px; bottom: 26px;
    text-align: right; font-size: 13px; color: var(--ink-soft); line-height: 18px;
  }
  .address .web { color: var(--blue); letter-spacing: 3px; }
</style>
</head>
<body>

<section class="card card-back">
  <div class="back-brand">
    <span class="dot"></span>
    <span class="name">Velqor5</span>
  </div>
  <p class="back-url">www.velqor5.com</p>
</section>

<section class="card card-front">
  <div class="name-band">
    <span class="person">Marin Tolk</span>
    <span class="role">President</span>
  </div>
  <div class="front-brand">
    <span class="dot"></span>
    <span class="name">Velqor5</span>
  </div>

  <ul class="contacts">
    <li>
      <svg viewBox="0 0 16 16" aria-hidden="true"><path d="M2 5c0-2 2-3 6-3s6 1 6 3v1h-3V5H5v1H2zM4 7h8l2 7H2z"/></svg>
      412 6390 1847
    </li>
    <li>
      <svg viewBox="0 0 16 16" aria-hidden="true"><path d="M4 1h8v14H4zM5.5 3v9h5V3zM7 13h2v1H7z" fill-rule="evenodd"/></svg>
      739 2084 6613
    </li>
    <li>
      <svg viewBox="0 0 16 16" aria-hidden="true"><path d="M4 1h8v4H4zM1 6h14v6h-3v3H4v-3H1zM5 10v3h6v-3z" fill-rule="evenodd"/></svg>
      625 9031 4472
    </li>
    <li>
      <svg viewBox="0 0 16 16" aria-hidden="true"><path d="M1 3h14v2L8 9 1 5zM1 6.5l7 4 7-4V13H1z"/></svg>
      marin@velqor5.com
    </li>
  </ul>

  <address class="address" style="font-style:normal">
    2716 Harrowgate Lane<br>
    Brookvale, NJ 07410<br>
    <span class="web">www.velqor5.com</span>
  </address>
</section>

</body>
</html>
```